Looking for a website homepage design

Hi, we are looking for a design for Homepage for our childcare centre
We want something really progressive, edgy, modern and premium. We want this website to standout but not cluttered. We only need a Homepage.
1366 Wx768 H
The call to action is join our community
We like the idea of a split screen
Divided into section
Locations and Enrolments
Lantern
Careers
Partnerships
We like angles and shapes, particularly triangles in the designs
Our company font is Hands of Sean
Have attached some designs that we like the look and feel of and some of our designs from our flyers and some images to use, you don't need to choose all the images, just whatever works with your design.
We have a STEM focus at our centres so something sciencey would be great.
Consider in the design will be viewed on desktop and mobile phones

Industry/Entity Type

childcare with Science focus

Number of Pages Required

1 page

Font styles to use
Other font styles liked:
• hands of sean is our company font

Requirements
Must have
• Homepage for website
Nice to have
• Split screen design

```html
<!DOCTYPE html>
<html lang="en">
<head>
<meta charset="utf-8">
<title>Bright Sprouts Kindergarten – Homepage</title>
<link rel="stylesheet" href="https://fonts.googleapis.com/css2?family=Gochi+Hand&family=Poppins:wght@400;500&family=Roboto:wght@400&display=swap">
<style>
  :root {
    --stage: #fca35f;
    --sun-yellow: #fff200;
    --sky-blue: #00aeef;
    --coral-red: #ef4a3f;
    --ink-navy: #2b3a55;
    --body-grey: #5b5b5b;
    --white: #ffffff;
    --photo-dark: #1d2436;
  }
  * { box-sizing: border-box; margin: 0; padding: 0; }
  html, body { width: 1200px; height: 1200px; overflow: hidden; }
  body { background: var(--stage); position: relative; font-family: "Roboto", sans-serif; }

  .homepage {
    position: absolute; left: 0; top: 263px;
    width: 1200px; height: 674px; overflow: hidden;
    display: flex;
  }

  /* ---------- Left: community call to action ---------- */
  .community-panel { position: relative; width: 617px; height: 674px; background: var(--sun-yellow); overflow: hidden; }
  .community-shapes { position: absolute; inset: 0; }
  .brand-tile {
    position: absolute; left: 67px; top: 0; width: 106px; height: 100px;
    background: var(--sky-blue); border-radius: 0 0 8px 8px;
    display: flex; align-items: center; justify-content: center; text-align: center;
    font-family: "Gochi Hand", cursive; font-size: 20px; line-height: 20px; color: var(--sun-yellow);
  }
  .community-cta {
    position: absolute; left: 120px; top: 500px;
    font-family: "Gochi Hand", cursive; font-size: 42px; color: var(--white); letter-spacing: 1px;
  }

  /* ---------- Right: sections ---------- */
  .sections-panel { position: relative; width: 583px; height: 674px; }
  .stem-hero {
    position: absolute; left: 0; top: 0; width: 583px; height: 306px;
    background: linear-gradient(135deg, #2a3350 0%, #1d2436 45%, #4a4f63 75%, #23314a 100%);
    overflow: hidden;
  }
  .main-menu { position: absolute; top: 22px; left: 202px; display: flex; gap: 48px; list-style: none; }
  .main-menu li { font-family: "Poppins", sans-serif; font-size: 16px; color: var(--white); }
  .stem-headline {
    position: absolute; left: 48px; top: 166px;
    font-family: "Gochi Hand", cursive; font-size: 31px; line-height: 31px; color: var(--white);
  }
  .hero-corner { position: absolute; inset: 0; }

  .locations-band {
    position: absolute; left: 0; top: 306px; width: 583px; height: 120px;
    background: var(--sky-blue);
    display: flex; align-items: center; justify-content: center; gap: 14px;
    font-family: "Gochi Hand", cursive; font-size: 30px; color: var(--white); letter-spacing: 0.5px;
  }

  .section-tile { position: absolute; top: 426px; height: 248px; overflow: hidden; }
  .section-tile.career { left: 0; width: 296px; background: var(--sun-yellow); }
  .section-tile.partnership { left: 296px; width: 287px; background: var(--coral-red); }
  .tile-title {
    position: absolute; left: 48px; top: 68px; display: flex; align-items: center; gap: 8px;
    font-family: "Gochi Hand", cursive; font-size: 26px;
  }
  .career .tile-title { color: var(--ink-navy); }
  .partnership .tile-title { color: var(--white); }
  .tile-copy {
    position: absolute; left: 48px; top: 116px; width: 170px;
    font-size: 12px; line-height: 15px;
  }
  .career .tile-copy { color: var(--body-grey); }
  .partnership .tile-copy { color: var(--white); width: 160px; }
  .tile-shapes { position: absolute; inset: 0; }
</style>
</head>
<body>
<main class="homepage">

  <section class="community-panel">
    <svg class="community-shapes" width="617" height="674" viewBox="0 0 617 674">
      <path d="M0 498 L160 340 Q183 318 206 340 L306 432 Q316 440 330 440 L617 440 L617 674 L0 674 Z" fill="var(--sky-blue)"/>
      <g role="img" aria-label="Photo: young child in a white lab coat">
        <rect x="-12" y="179" width="176" height="176" rx="18" transform="rotate(45 76 267)" fill="#7d6a5e"/>
      </g>
      <g role="img" aria-label="Photo: smiling girl with face paint at a science activity">
        <rect x="352" y="106" width="290" height="290" rx="28" transform="rotate(45 497 251)" fill="#c8b3a8" stroke="var(--white)" stroke-width="4"/>
      </g>
      <polygon points="142,603 222,603 182,640" fill="var(--sun-yellow)"/>
      <polygon points="0,590 22,620 0,648" fill="var(--sun-yellow)"/>
    </svg>
    <div class="brand-tile">Bright<br>Sprouts</div>
    <h1 class="community-cta">Join Our Community</h1>
  </section>

  <section class="sections-panel">
    <div class="stem-hero">
      <div role="img" aria-label="Photo: children in lab coats exploring a sand volcano table" style="position:absolute;inset:0;"></div>
      <svg class="hero-corner" width="583" height="306" viewBox="0 0 583 306">
        <polygon points="400,306 583,140 583,306" fill="var(--sun-yellow)"/>
        <polygon points="45,100 68,100 56,116" fill="var(--sun-yellow)"/>
      </svg>
      <ul class="main-menu">
        <li>Menu 1</li><li>Menu 2</li><li>Menu 3</li>
      </ul>
      <h2 class="stem-headline">Presenting Lantern<br>an industry first<br>pioneering, STEM Hub</h2>
    </div>

    <a class="locations-band">Locations and Enrolments
      <svg width="36" height="22" viewBox="0 0 36 22"><path d="M2 11 H32 M22 2 L33 11 L22 20" fill="none" stroke="var(--white)" stroke-width="3" stroke-linecap="round" stroke-linejoin="round"/></svg>
    </a>

    <article class="section-tile career">
      <svg class="tile-shapes" width="296" height="248" viewBox="0 0 296 248">
        <polygon points="260,50 280,58 262,66" fill="var(--coral-red)"/>
        <polygon points="20,232 36,200 64,232" fill="var(--coral-red)"/>
      </svg>
      <h3 class="tile-title">Career
        <svg width="26" height="18" viewBox="0 0 26 18"><path d="M2 9 H23 M15 2 L23 9 L15 16" fill="none" stroke="var(--ink-navy)" stroke-width="2.5" stroke-linecap="round" stroke-linejoin="round"/></svg>
      </h3>
      <p class="tile-copy">We're always looking for the right people to join the Bright Sprouts™ family. If there isn't a suitable role available right now,</p>
    </article>

    <article class="section-tile partnership">
      <svg class="tile-shapes" width="287" height="248" viewBox="0 0 287 248">
        <polygon points="96,248 148,190 200,248" fill="var(--sky-blue)"/>
      </svg>
      <h3 class="tile-title">Partnership
        <svg width="26" height="18" viewBox="0 0 26 18"><path d="M2 9 H23 M15 2 L23 9 L15 16" fill="none" stroke="var(--white)" stroke-width="2.5" stroke-linecap="round" stroke-linejoin="round"/></svg>
      </h3>
      <p class="tile-copy">We look forward to welcoming your child to the Bright Sprouts™ family!</p>
    </article>
  </section>

</main>
</body>
</html>
```